I need a two page flyer (one page front and back) outlining our residential furniture rental options.

Title: Premium Residential Furniture Rentals

GOOD
Our Bellmore Ridge Furniture Package is designed to offer a perfect balance of affordability and style, without compromising on quality. This package features a selection of functional and aesthetically pleasing furniture pieces, ideal for those looking to create a polished and professional space. With quick installation handled by our experienced in-house team, you can expect a smooth and hassle-free setup. This package ensures both convenience and value, providing a streamlined solution for your needs.
Living room, dining room and bedroom (additional bedrooms available)
- $710/month with a 3 month commitment
- $570/month with a 6 month commitment

BETTER
Our Premium Furniture Package takes comfort and style to the next level, offering an enhanced experience compared to our Bellmore option. Carefully selected with durability in mind, this package features high-quality, convenient furniture designed for both functionality and aesthetics. Perfect for those seeking a more refined look and superior comfort, it’s ideal for creating a sophisticated and inviting environment. With attention to detail in both design and craftsmanship, the premium package elevates any space, ensuring a higher standard of comfort and style that caters to both employees and clients.
- $1,150/month with a 3 month commitment
- $900/month with a 6 month commitment

BEST
Our Custom Furniture Package offers a tailored experience where you’ll work directly with our expert designer to create the ultimate luxurious and functional space. We include lounging, dining, sleeping and working from home, this package allows you to curate a space that perfectly fits your needs and style. With personalized attention to detail, we ensure every element is designed to provide the highest level of comfort, convenience, and elegance, transforming your space into a sophisticated sanctuary for relaxation and enjoyment.
Please inquire for pricing

www.quillbyhomeleasing.example

```html
<!DOCTYPE html>
<html lang="en">
<head>
<meta charset="UTF-8">
<title>Premium Residential Furniture Rentals – Flyer</title>
<link rel="stylesheet" href="https://fonts.googleapis.com/css2?family=Cinzel:wght@400&family=Great+Vibes&family=Open+Sans:wght@400;700&family=Montserrat:wght@500;800&display=swap">
<style>
  :root {
    --canvas: #e9e3d8;
    --ink-dark: #2b2c2e;
    --ink-deeper: #1c1d1f;
    --photo-dark-a: #4a4b4d;
    --photo-dark-b: #2e2f31;
    --white: #ffffff;
    --soft-white: #e8e8e8;
    --script-blue: #4aa3e0;
    --tick-red: #d62b2b;
    --heading-gray: #6b6b6b;
    --body-gray: #3c3c3c;
    --hex-brown: #6f5a45;
    --photo-room-a: #d9dcdf;
    --photo-room-b: #9ea2a6;
    --photo-warm-a: #b49b7e;
    --photo-warm-b: #5b4a3a;
  }
  * { box-sizing: border-box; margin: 0; padding: 0; }
  html, body { width: 1200px; height: 900px; overflow: hidden; }
  body { background: var(--canvas); position: relative; font-family: "Open Sans", sans-serif; }

  .page { position: absolute; top: 68px; width: 540px; height: 764px; overflow: hidden; box-shadow: 0 6px 18px rgba(0,0,0,.18); }
  .page--front { left: 40px; background: var(--ink-dark); color: var(--white); }
  .page--back { left: 620px; background: var(--white); color: var(--body-gray); }

  /* FRONT */
  .front-photo { position: absolute; inset: 0; background: linear-gradient(160deg, var(--photo-dark-a) 0%, #3b3c3e 45%, var(--photo-dark-b) 100%); }
  .front-content { position: absolute; left: 96px; right: 30px; top: 40px; }
  .title { font-family: "Cinzel", serif; font-weight: 400; font-size: 31px; letter-spacing: 1px; line-height: 1; text-align: center; }
  .title-script { font-family: "Great Vibes", cursive; color: var(--script-blue); font-size: 38px; text-align: center; margin-top: 2px; line-height: 1.1; }
  .tier { margin-top: 16px; font-size: 8.6px; line-height: 1.5; color: var(--soft-white); }
  .tier p { text-align: justify; }
  .tier-rooms { font-weight: 700; margin-top: 5px; color: var(--white); }
  .price { display: flex; align-items: center; gap: 5px; font-weight: 700; color: var(--white); }
  .tick { width: 9px; height: 9px; flex: none; }
  .tier-ladder { position: absolute; left: 24px; top: 198px; width: 44px; height: 470px; }
  .ladder-inner { position: absolute; left: 50%; top: 50%; width: 470px; height: 30px; transform: translate(-50%,-50%) rotate(-90deg); display: flex; align-items: center; gap: 10px; font-family: "Montserrat", sans-serif; font-weight: 800; font-size: 17px; letter-spacing: 1px; }
  .ladder-line { flex: 1; height: 1.5px; background: var(--white); }
  .front-band { position: absolute; left: 0; right: 0; bottom: 0; height: 60px; background: var(--ink-deeper); display: flex; align-items: center; justify-content: center; font-family: "Montserrat", sans-serif; font-weight: 500; font-size: 14px; letter-spacing: 1px; }

  /* BACK */
  .hero-photo { position: absolute; left: 0; top: 0; width: 540px; height: 330px; background: linear-gradient(180deg, var(--photo-room-a) 0%, #c3c6c9 60%, var(--photo-room-b) 100%); }
  .hero-fade { position: absolute; left: 0; top: 0; }
  .inset-photo { position: absolute; border: 4px solid var(--white); }
  .inset-photo--living { left: 80px; top: 210px; width: 150px; height: 118px; background: linear-gradient(160deg, var(--photo-room-a), var(--photo-warm-a) 70%, var(--photo-warm-b)); }
  .inset-photo--dining { left: 200px; top: 160px; width: 140px; height: 120px; background: linear-gradient(170deg, #eef0f1, #a7abaf 80%); }
  .inset-photo--kitchen { left: 350px; top: 105px; width: 140px; height: 110px; background: linear-gradient(160deg, #e3e4e4, var(--photo-warm-b) 85%); }
  .hex-frame { position: absolute; left: 0; top: 128px; }
  .brand { position: absolute; left: 22px; top: 176px; width: 120px; text-align: center; display: flex; flex-direction: column; align-items: center; gap: 5px; }
  .brand-square { width: 22px; height: 22px; border: 1.5px solid var(--ink-dark); }
  .brand-name { font-family: "Montserrat", sans-serif; font-weight: 500; font-size: 8.5px; letter-spacing: 1px; color: var(--ink-dark); line-height: 1.3; }
  .services { position: absolute; left: 0; right: 0; top: 360px; text-align: center; font-family: "Cinzel", serif; font-size: 28px; line-height: 1.15; color: var(--heading-gray); letter-spacing: 1px; }
  .about { position: absolute; left: 40px; right: 40px; top: 442px; font-size: 10.2px; line-height: 1.6; text-align: center; }
  .contact { position: absolute; left: 34px; right: 34px; top: 628px; display: flex; align-items: center; gap: 14px; font-family: "Montserrat", sans-serif; }
  .contact-title { font-weight: 800; font-size: 18px; color: var(--ink-deeper); }
  .phone { display: flex; align-items: center; gap: 6px; font-weight: 800; font-size: 17px; color: var(--ink-deeper); }
  .address { margin-left: auto; display: flex; align-items: center; gap: 5px; font-size: 8px; line-height: 1.4; font-weight: 500; }
  .back-band { position: absolute; left: 0; right: 0; bottom: 0; height: 58px; background: var(--ink-dark); color: var(--white); display: flex; align-items: center; gap: 8px; padding-left: 30px; font-family: "Montserrat", sans-serif; font-size: 10px; font-weight: 500; }
</style>
</head>
<body>

<section class="page page--front">
  <div class="front-photo" role="img" aria-label="Photograph of a furnished living room, darkened behind the text"></div>

  <div class="tier-ladder">
    <div class="ladder-inner">
      <span>BEST</span><span class="ladder-line"></span><span>BETTER</span><span class="ladder-line"></span><span>GOOD</span>
    </div>
  </div>

  <div class="front-content">
    <h1 class="title">PREMIUM RESIDENTIAL</h1>
    <div class="title-script">Furniture Rentals</div>

    <div class="tier tier--good">
      <p>Our Bellmore Ridge Furniture Package is designed to offer a perfect balance of affordability and style, without compromising on quality. This package features a selection of functional and aesthetically pleasing furniture pieces, ideal for those looking to create a polished and professional space. With quick installation handled by our experienced in-house team, you can expect a smooth and hassle-free setup. This package ensures both convenience and value, providing a streamlined solution for your needs.</p>
      <div class="tier-rooms">Living room, dining room and bedroom (additional bedrooms available)</div>
      <div class="price"><svg class="tick" viewBox="0 0 10 10"><rect width="10" height="10" rx="1.5" fill="var(--tick-red)"/><path d="M2 5.2 4.2 7.3 8 2.8" stroke="#fff" stroke-width="1.4" fill="none"/></svg>$710/month with a 3 month commitment</div>
      <div class="price"><svg class="tick" viewBox="0 0 10 10"><rect width="10" height="10" rx="1.5" fill="var(--tick-red)"/><path d="M2 5.2 4.2 7.3 8 2.8" stroke="#fff" stroke-width="1.4" fill="none"/></svg>$570/month with a 6 month commitment</div>
    </div>

    <div class="tier tier--better">
      <p>Our Premium Furniture Package takes comfort and style to the next level, offering an enhanced experience compared to our Bellmore option. Carefully selected with durability in mind, this package features high-quality, convenient furniture designed for both functionality and aesthetics. Perfect for those seeking a more refined look and superior comfort, it’s ideal for creating a sophisticated and inviting environment. With attention to detail in both design and craftsmanship, the premium package elevates any space, ensuring a higher standard of comfort and style that caters to both employees and clients.</p>
      <div class="tier-rooms">Living room, dining room and bedroom (additional bedrooms available)</div>
      <div class="price"><svg class="tick" viewBox="0 0 10 10"><rect width="10" height="10" rx="1.5" fill="var(--tick-red)"/><path d="M2 5.2 4.2 7.3 8 2.8" stroke="#fff" stroke-width="1.4" fill="none"/></svg>$1,150/month with a 3 month commitment</div>
      <div class="price"><svg class="tick" viewBox="0 0 10 10"><rect width="10" height="10" rx="1.5" fill="var(--tick-red)"/><path d="M2 5.2 4.2 7.3 8 2.8" stroke="#fff" stroke-width="1.4" fill="none"/></svg>$900/month with a 6 month commitment</div>
    </div>

    <div class="tier tier--best">
      <p>Our Custom Furniture Package offers a tailored experience where you’ll work directly with our expert designer to create the ultimate luxurious and functional space. We include lounging, dining, sleeping and working from home, this package allows you to curate a space that perfectly fits your needs and style. With personalized attention to detail, we ensure every element is designed to provide the highest level of comfort, convenience, and elegance, transforming your space into a sophisticated sanctuary for relaxation and enjoyment.</p>
      <div class="tier-rooms">Living room, dining room and bedroom (additional bedrooms available)</div>
      <div class="price"><svg class="tick" viewBox="0 0 10 10"><rect width="10" height="10" rx="1.5" fill="var(--tick-red)"/><path d="M2 5.2 4.2 7.3 8 2.8" stroke="#fff" stroke-width="1.4" fill="none"/></svg>$710/month with a 3 month commitment</div>
      <div class="price"><svg class="tick" viewBox="0 0 10 10"><rect width="10" height="10" rx="1.5" fill="var(--tick-red)"/><path d="M2 5.2 4.2 7.3 8 2.8" stroke="#fff" stroke-width="1.4" fill="none"/></svg>$570/month with a 6 month commitment</div>
    </div>
  </div>

  <div class="front-band">PLEASE INQUIRE FOR PRICING</div>
</section>

<section class="page page--back">
  <div class="hero-photo" role="img" aria-label="Photograph of a bright open-plan furnished living space with ceiling fan"></div>
  <svg class="hero-fade" width="540" height="360" viewBox="0 0 540 360" aria-hidden="true">
    <path d="M0 300 L540 250 L540 360 L0 360 Z" fill="var(--white)"/>
  </svg>
  <div class="inset-photo inset-photo--living" role="img" aria-label="Photograph of a living room with sofa and wall clock"></div>
  <div class="inset-photo inset-photo--dining" role="img" aria-label="Photograph of a dining area with chairs"></div>
  <div class="inset-photo inset-photo--kitchen" role="img" aria-label="Photograph of a kitchen with dark cabinets"></div>

  <svg class="hex-frame" width="170" height="170" viewBox="0 0 170 170" aria-hidden="true">
    <polygon points="85,4 158,45 158,125 85,166 12,125 12,45" fill="var(--white)" stroke="var(--hex-brown)" stroke-width="5"/>
  </svg>
  <div class="brand">
    <span class="brand-square"></span>
    <span class="brand-name">QUILLBY HOME LEASING</span>
  </div>

  <h2 class="services">STAGING | RESIDENTIAL<br>CORPORATE | SALES</h2>

  <p class="about">Since its founding in 2009, Quillby Home Leasing &amp; Sales has been a trusted provider of quality furniture and staging services. In October 2021, the company was acquired and, in 2023, underwent a significant transformation by merging with Harbor Home Furnishings and rebranding as Quillby Home Leasing. We remain committed to delivering top-notch services, competitive pricing, and outstanding customer support. While we take pride in our rich history, we're also excited for the future and look forward to continuing to serve our customers with the same dedication and excellence that has defined us from the start.</p>

  <div class="contact">
    <span class="contact-title">CONTACT US</span>
    <span class="phone">
      <svg width="20" height="20" viewBox="0 0 20 20" aria-hidden="true"><circle cx="10" cy="10" r="10" fill="var(--ink-deeper)"/><path d="M7 5.5c-.6 0-1.3.7-1.2 1.6.3 3 3.6 6.3 6.6 6.6.9.1 1.6-.6 1.6-1.2l-1.8-1.2-1.1.8c-1.1-.5-2.6-2-3.1-3.1l.8-1.1z" fill="#fff"/></svg>
      +1 555-014-0833
    </span>
    <span class="address">
      <svg width="12" height="16" viewBox="0 0 12 16" aria-hidden="true"><path d="M6 1a5 5 0 0 0-5 5c0 4 5 9 5 9s5-5 5-9a5 5 0 0 0-5-5z" fill="none" stroke="var(--body-gray)" stroke-width="1.2"/><circle cx="6" cy="6" r="1.8" fill="var(--body-gray)"/></svg>
      <span>418 Alder Point Road #204,<br>Lakeview, Texas 77000, United States</span>
    </span>
  </div>

  <div class="back-band">
    <svg width="16" height="16" viewBox="0 0 16 16" aria-hidden="true"><circle cx="8" cy="8" r="7" fill="none" stroke="#fff" stroke-width="1.2"/><path d="M1 8h14M8 1c-3 3.5-3 10.5 0 14M8 1c3 3.5 3 10.5 0 14" stroke="#fff" stroke-width="1" fill="none"/></svg>
    www.quillbyhomeleasing.example
  </div>
</section>

</body>
</html>
```